Rollo Penwick Design, LLC (www.rollopenwick.example)

A very hip, trendy architectural home page. Simple Menu upper right hand corner (About, Projects, Inspiration, Design-Build, Contact). In the "Projects" ... I want to click on each project and that will open up multiple photo's of that project. Attached are the graphics of my logo. I want the home page to be incredible ... I really market my name "Rollo Penwick" as sophisticated architecture. Colors/branding should be black/metallic/white/grey maybe with a pop of a bright color but not much. My architecture is like www.brantleyhoweatelier.example if you want to review as example. My specialty is industrial design, homes with architectural concrete design, steel beams, alot of glass. Very modern. My work is best illustrated at www.varnellquist.example.
Updates

Please see images uploaded in my brief. A new business card design by an AWESOME designer and some inspirational architectural projects I worked on.

Industry/Entity Type

Architecture

Coding

Coded - Design and coding required

Number of Pages Required

5+ page

Colors

Designer to choose only greyscale colors for use in the design.

Requirements
Must have
• The 1st project photo gallery is called "Foundry Dwelling by the Gulf Shore"... Images of this project can be taken from: https://www.hearthlisto.example/homedetails/2873-9th-St-SE-Naples-FL-34102/508164290_zpid/

The 2nd project photo gallery is called "Stone, Iron and Pane Residences of the Gulf Shore". I will upload images for this project but use placeholder until I finalize.

The 3rd photo gallery is called "Early Sketches: Off the Drafting Table". I will forward pictures. for this.

Website should be easy to update and handover at completion as we will be updating frequently. Wordpress, WIX, or other type is fine as long as it looks profesional and high-class.
Nice to have
• Maybe the home page loads to just "Rollo Penwick Design, LLC ... Workshop of Inventive Structural Vision" and has a click to enter button. Something cool maybe a fade it or something eye-catching and cool.
Should not have
• Should not be overly colorful.

```html
<!DOCTYPE html>
<html lang="en">
<head>
<meta charset="utf-8">
<title>Rollo Penwick Design, LLC</title>
<link rel="stylesheet" href="https://fonts.googleapis.com/css2?family=Playfair+Display:wght@700&family=Poppins:wght@200;300;400;500;600&display=swap">
<style>
:root{
  --bg:#1c1f25;
  --text:#ffffff;
  --muted:#d6d8dc;
  --rule:#5a5e66;
  --dot:#8a8f98;
  --outline:#a3a8b0;
}
*{box-sizing:border-box;margin:0;padding:0}
html,body{width:1200px;height:3431px;overflow:hidden;background:var(--bg)}
body{position:relative;color:var(--text);font-family:"Poppins",sans-serif}
.abs{position:absolute}

/* header */
.site-header{position:absolute;left:0;top:0;width:1200px;height:83px;border-bottom:1px solid var(--rule)}
.brand{position:absolute;display:flex;align-items:center;gap:10px;font-family:"Poppins",sans-serif;font-weight:400;color:var(--text)}
.brand-mark{width:34px;height:34px;border:2px solid var(--text)}
.brand-name{font-size:15px;letter-spacing:.5px}
.main-nav a{position:absolute;top:33px;font-size:15px;color:var(--text);text-decoration:none;font-weight:400}

/* hero */
.hero-photo{left:531px;top:125px;width:669px;height:428px;background:linear-gradient(180deg,#4a4d52 0%,#2c2e31 45%,#55575a 70%,#1e1f21 100%)}
.hero-year{left:60px;top:178px;font-size:50px;font-weight:200;color:var(--muted)}
.hero-title{left:62px;top:242px;font-family:"Playfair Display",serif;font-weight:700;font-size:73px;line-height:93px;color:var(--text);white-space:nowrap}
.btn{position:absolute;display:flex;align-items:center;justify-content:center;border:2px solid var(--text);border-radius:2px;color:var(--text);font-size:17px;font-weight:400}
.btn-about{left:62px;top:455px;width:147px;height:47px}

/* about */
.about-photo{left:0;top:678px;width:341px;height:457px;background:radial-gradient(ellipse at 60% 45%,#6f6f6f 0%,#3a3a3a 40%,#161616 100%)}
.section-title{position:absolute;font-family:"Playfair Display",serif;font-weight:700;font-size:49px;color:var(--text);white-space:nowrap}
.rule{position:absolute;height:1px;background:var(--rule)}
.about-copy{left:433px;top:755px;width:601px;font-size:17.5px;line-height:26.6px;color:var(--muted);text-align:justify;font-weight:400}
.about-copy p{margin-bottom:25px}
.social-side span{position:absolute;width:34px;height:34px;border:3px solid var(--text);border-radius:8px}

/* projects */
.project-title{position:absolute;font-size:35px;font-weight:500;line-height:50px;color:transparent;-webkit-text-stroke:1px var(--outline);white-space:nowrap}
.project-title span{display:block}
.specs{position:absolute;font-size:17.5px;color:var(--muted)}
.specs b{font-weight:600;color:var(--text)}
.specs .row{position:absolute;white-space:nowrap}
.desc{position:absolute;font-size:17.5px;line-height:26.6px;color:var(--muted);text-align:justify}
.project-photo{position:absolute}
.photo-one{left:622px;top:1324px;width:578px;height:400px;background:linear-gradient(180deg,#1d2a66 0%,#2e3d7c 35%,#8a7a58 60%,#6d604a 88%,#3f6b3a 100%)}
.photo-two{left:5px;top:1889px;width:578px;height:401px;background:linear-gradient(180deg,#1f4f96 0%,#4f7fbf 35%,#d3cfc4 55%,#b8893a 75%,#6a3a2a 100%)}
.photo-three{left:617px;top:2423px;width:583px;height:397px;background:linear-gradient(180deg,#c9ccd1 0%,#e6e7e9 40%,#a3a4a6 70%,#8c8c8d 100%)}
.pager{position:absolute;display:flex;align-items:center;gap:18px;font-size:17px;color:var(--text)}
.btn-more{left:511px;top:2965px;width:178px;height:45px;font-size:17px}

/* footer */
.site-footer{position:absolute;left:0;top:3064px;width:1200px;height:367px;border-top:1px solid var(--rule)}
.contact-line{position:absolute;left:44px;display:flex;align-items:flex-start;gap:14px;font-size:11.5px;line-height:17px;color:var(--muted)}
.footer-label{position:absolute;font-size:13.5px;font-weight:600;color:var(--text)}
.social-foot span{position:absolute;top:110px;width:36px;height:36px;border:3px solid var(--text);border-radius:8px}
.newsletter{position:absolute;left:797px;top:86px;width:342px;height:49px;border:1px solid var(--text);border-radius:3px;display:flex}
.newsletter .field{flex:1;display:flex;align-items:center;padding-left:16px;font-size:12px;color:var(--muted)}
.newsletter .go{width:60px;border-left:1px solid var(--text);display:flex;align-items:center;justify-content:center;font-size:14px;font-weight:600}
.copyright{position:absolute;left:0;top:309px;width:1200px;border-top:1px solid var(--rule);padding-top:20px;text-align:center;font-size:14px;font-weight:600}
</style>
</head>
<body>

<header class="site-header">
  <div class="brand" style="left:63px;top:22px">
    <span class="brand-mark"></span>
    <span class="brand-name">Rollo Penwick Design</span>
  </div>
  <nav class="main-nav">
    <a style="left:522px">Home</a>
    <a style="left:613px">About</a>
    <a style="left:703px">Projects</a>
    <a style="left:810px">Inspiration</a>
    <a style="left:935px">Design-build</a>
    <a style="left:1078px">Contact</a>
  </nav>
</header>

<section class="hero">
  <div class="abs hero-photo" role="img" aria-label="Modern concrete and glass house among dark pines at dusk"></div>
  <div class="abs hero-year">/2021</div>
  <h1 class="abs hero-title">Workshop of Inventive<br>Structural Vision.</h1>
  <div class="btn btn-about">About</div>
  <svg class="abs" style="left:500px;top:455px" width="150" height="130">
    <defs><pattern id="dots-hero" width="20" height="20" patternUnits="userSpaceOnUse"><circle cx="2" cy="2" r="1.8" fill="#8a8f98"/></pattern></defs>
    <rect x="0" y="0" width="40" height="120" fill="url(#dots-hero)"/>
    <rect x="0" y="120" width="150" height="10" fill="url(#dots-hero)"/>
  </svg>
</section>

<section class="about">
  <div class="abs about-photo" role="img" aria-label="Black and white portrait of the architect"></div>
  <svg class="abs" style="left:255px;top:1066px" width="150" height="130">
    <defs><pattern id="dots-about" width="20" height="20" patternUnits="userSpaceOnUse"><circle cx="2" cy="2" r="1.8" fill="#8a8f98"/></pattern></defs>
    <rect x="100" y="0" width="50" height="130" fill="url(#dots-about)"/>
    <rect x="0" y="80" width="150" height="50" fill="url(#dots-about)"/>
  </svg>
  <h2 class="section-title" style="left:433px;top:674px">About me</h2>
  <div class="rule" style="left:653px;top:712px;width:381px"></div>
  <div class="abs about-copy">
    <p>Hi, i'am Rollo Penwick an architect. My specialty is industrial design, homes with architectural concrete design, steel beams, alot of glass. I have spent 10 years in designing and developing innovative consumer products in many industries.</p>
    <p>Lorem ipsum dolor sit amet, consectetur adipiscing elit, sed do eiusmod tempor incididunt ut labore et dolore magna aliqua. Ut enim ad minim veniam, quis nostrud exercitation ullamco laboris nisi ut aliquip ex ea commodo consequat.</p>
    <p>Duis aute irure dolor in reprehenderit in voluptate velit esse cillum dolore eu fugiat nulla pariatur.</p>
  </div>
  <div class="social-side" aria-label="Social profiles">
    <span style="left:1102px;top:802px"></span>
    <span style="left:1102px;top:883px;border-radius:50%"></span>
    <span style="left:1102px;top:969px"></span>
  </div>
</section>

<section class="projects">
  <div class="rule" style="left:622px;top:1275px;width:325px"></div>
  <h2 class="section-title" style="left:968px;top:1244px">Projects</h2>

  <!-- project 01 -->
  <h3 class="project-title" style="left:44px;top:1324px"><span>01 / Foundry Dwelling by</span><span style="padding-left:67px">the Gulf Shore</span></h3>
  <div class="specs" style="left:44px;top:1472px">
    <div class="row" style="left:0;top:0"><b>AREA :</b> 13.200 sqft</div>
    <div class="row" style="left:212px;top:0"><b>TYPE&nbsp; :</b> Single famili residence</div>
    <div class="row" style="left:0;top:41px"><b>YEAR&nbsp; :</b> 2016</div>
    <div class="row" style="left:212px;top:41px"><b>LOCATION :</b> Florida</div>
    <div class="row" style="left:0;top:100px"><b>Desc&nbsp; :</b> Florida</div>
  </div>
  <p class="desc" style="left:44px;top:1606px;width:466px">H2082 - A stunning and sophisticated Contemporary Estate on 2.5 acres of land, nearing Final Completion, with meticulous attention to design and detail. This Architectural Masterpiece boasts over 10,000 sq. ft. with 7 Bedrooms and 7 Bathrooms in the main residence and over 2800 sq. ft. with 3 Bedrooms and 2 Bathrooms in the second residence.</p>
  <div class="project-photo photo-one" role="img" aria-label="Concrete panel house with glass entrance lit at night"></div>
  <svg class="abs" style="left:564px;top:1636px" width="150" height="130">
    <defs><pattern id="dots-p1" width="20" height="20" patternUnits="userSpaceOnUse"><circle cx="2" cy="2" r="1.8" fill="#8a8f98"/></pattern></defs>
    <rect x="0" y="0" width="50" height="130" fill="url(#dots-p1)"/>
    <rect x="0" y="80" width="150" height="50" fill="url(#dots-p1)"/>
  </svg>
  <div class="pager" style="left:848px;top:1739px">
    <svg width="18" height="14" viewBox="0 0 18 14"><path d="M17 7H2M7 1L1 7l6 6" fill="none" stroke="#fff" stroke-width="1.8"/></svg>
    <span>1 of 10</span>
    <svg width="18" height="14" viewBox="0 0 18 14"><path d="M1 7h15M11 1l6 6-6 6" fill="none" stroke="#fff" stroke-width="1.8"/></svg>
  </div>

  <!-- project 02 -->
  <div class="project-photo photo-two" role="img" aria-label="Glass and steel pavilion glowing at dusk beside a concrete wing"></div>
  <svg class="abs" style="left:497px;top:2206px" width="150" height="130">
    <defs><pattern id="dots-p2" width="20" height="20" patternUnits="userSpaceOnUse"><circle cx="2" cy="2" r="1.8" fill="#8a8f98"/></pattern></defs>
    <rect x="100" y="0" width="50" height="130" fill="url(#dots-p2)"/>
    <rect x="0" y="100" width="150" height="30" fill="url(#dots-p2)"/>
  </svg>
  <div class="pager" style="left:206px;top:2307px">
    <svg width="18" height="14" viewBox="0 0 18 14"><path d="M17 7H2M7 1L1 7l6 6" fill="none" stroke="#fff" stroke-width="1.8"/></svg>
    <span>1 of 5</span>
    <svg width="18" height="14" viewBox="0 0 18 14"><path d="M1 7h15M11 1l6 6-6 6" fill="none" stroke="#fff" stroke-width="1.8"/></svg>
  </div>
  <h3 class="project-title" style="left:626px;top:1889px"><span>02 / Stone, Iron and Pane</span><span style="padding-left:71px">Residences of the Gulf</span><span style="padding-left:71px">Shore</span></h3>
  <div class="specs" style="left:686px;top:2086px">
    <div class="row" style="left:0;top:0"><b>AREA :</b> 13.200 sqft</div>
    <div class="row" style="left:210px;top:0"><b>TYPE&nbsp; :</b> Single famili residence</div>
    <div class="row" style="left:0;top:41px"><b>YEAR&nbsp; :</b> 2016</div>
    <div class="row" style="left:210px;top:41px"><b>LOCATION :</b> Florida</div>
    <div class="row" style="left:0;top:100px"><b>Desc&nbsp; :</b> Florida</div>
  </div>
  <p class="desc" style="left:686px;top:2221px;width:466px">H2082 - A stunning and sophisticated Contemporary Estate on 2.5 acres of land, nearing Final Completion, with meticulous attention to design and detail.</p>

  <!-- project 03 -->
  <h3 class="project-title" style="left:44px;top:2423px"><span>03 / Early Sketches: Off the</span><span style="padding-left:75px">Drafting Table</span></h3>
  <div class="specs" style="left:44px;top:2570px">
    <div class="row" style="left:0;top:0"><b>AREA :</b> 13.200 sqft</div>
    <div class="row" style="left:212px;top:0"><b>TYPE&nbsp; :</b> Single famili residence</div>
    <div class="row" style="left:0;top:41px"><b>YEAR&nbsp; :</b> 2016</div>
    <div class="row" style="left:212px;top:41px"><b>LOCATION :</b> Florida</div>
    <div class="row" style="left:0;top:100px"><b>Desc&nbsp; :</b> Florida</div>
  </div>
  <p class="desc" style="left:44px;top:2705px;width:466px">H2082 - A stunning and sophisticated Contemporary Estate on 2.5 acres of land, nearing Final Completion, with meticulous attention to design and detail.</p>
  <div class="project-photo photo-three" role="img" aria-label="Bright open kitchen with a concrete island and pendant lights"></div>
  <svg class="abs" style="left:557px;top:2731px" width="150" height="130">
    <defs><pattern id="dots-p3" width="20" height="20" patternUnits="userSpaceOnUse"><circle cx="2" cy="2" r="1.8" fill="#8a8f98"/></pattern></defs>
    <rect x="0" y="0" width="50" height="130" fill="url(#dots-p3)"/>
    <rect x="0" y="80" width="150" height="50" fill="url(#dots-p3)"/>
  </svg>
  <div class="pager" style="left:858px;top:2836px">
    <svg width="18" height="14" viewBox="0 0 18 14"><path d="M17 7H2M7 1L1 7l6 6" fill="none" stroke="#fff" stroke-width="1.8"/></svg>
    <span>1 of 10</span>
    <svg width="18" height="14" viewBox="0 0 18 14"><path d="M1 7h15M11 1l6 6-6 6" fill="none" stroke="#fff" stroke-width="1.8"/></svg>
  </div>

  <div class="btn btn-more">VIEW MORE</div>
</section>

<footer class="site-footer">
  <div class="brand" style="left:44px;top:36px">
    <span class="brand-mark"></span>
    <span class="brand-name">Rollo Penwick Design</span>
  </div>
  <div class="rule" style="left:44px;top:113px;width:200px"></div>
  <div class="contact-line" style="top:138px">
    <svg width="16" height="18" viewBox="0 0 16 18"><path d="M8 17s6-6 6-10A6 6 0 0 0 2 7c0 4 6 10 6 10z" fill="none" stroke="#fff" stroke-width="1.4"/><circle cx="8" cy="7" r="2.2" fill="none" stroke="#fff" stroke-width="1.4"/></svg>
    <span>1480 MARROWIND BAY ROAD SUITE 312,<br>NAPLES FL 34108</span>
  </div>
  <div class="contact-line" style="top:186px">
    <svg width="16" height="16" viewBox="0 0 16 16"><path d="M3 1h3l1.5 4-2 1.2a9 9 0 0 0 4.3 4.3L11 8.5l4 1.5v3a2 2 0 0 1-2 2A12 12 0 0 1 1 3a2 2 0 0 1 2-2z" fill="none" stroke="#fff" stroke-width="1.3"/></svg>
    <span>2399 - 5550 - 1184</span>
  </div>
  <div class="contact-line" style="top:222px">
    <svg width="16" height="14" viewBox="0 0 16 14"><rect x="1" y="1.5" width="14" height="11" fill="none" stroke="#fff" stroke-width="1.3"/><path d="M1 2l7 6 7-6" fill="none" stroke="#fff" stroke-width="1.3"/></svg>
    <span>rollo@rollopenwick.example</span>
  </div>

  <div class="footer-label" style="left:466px;top:50px">FOLLOW US :</div>
  <div class="social-foot" aria-label="Social profiles">
    <span style="left:468px"></span>
    <span style="left:548px;border-radius:50%"></span>
    <span style="left:633px"></span>
  </div>

  <div class="footer-label" style="left:797px;top:46px">NEWSLETTER :</div>
  <div class="newsletter">
    <div class="field">Your email address</div>
    <div class="go">Go!</div>
  </div>

  <div class="copyright">ROLLO PENWICK DESIGN LLC - 2021 | ALL RIGHT RESERVED</div>
</footer>

</body>
</html>
```